Broschüre für Hausmeisterservice
Zielgruppe
Unser Hausmeisterservice bietet zuverlässige und professionelle Dienstleistungen rund um die Immobilie. Dazu gehören unter anderem die Pflege und Wartung von Gebäuden, kleinere Reparaturen, Reinigungsarbeiten, Gartenpflege sowie Winterdienst. Unser Ziel ist es, Eigentümern, Hausverwaltungen und Unternehmen einen sorgenfreien Rundum-Service zu bieten, damit ihre Immobilien stets gepflegt und funktionstüchtig sind. Unsere Zielgruppe sind somit Hausverwaltungen, Eigentümergemeinschaften, Firmen und Privatpersonen, die Wert auf eine gepflegte Immobilie legen und einen zuverlässigen Partner suchen.
Aufgabenstellung
Corporate Design und Kommunikation:
Freundlich, vertrauenswürdig und professionell wirken
Klare, verständliche Sprache verwenden
Visuelle Elemente, die Sauberkeit, Ordnung und gepflegte Immobilien ausstrahlen
Call-to-Action:
Klare Aufforderungen zur Kontaktaufnahme, Angebotserstellung oder Terminvereinbarung.

```html
<!DOCTYPE html>
<html lang="en">
<head>
<meta charset="utf-8">
<title>Caretaker Service Brochure</title>
<link rel="stylesheet" href="https://fonts.googleapis.com/css2?family=Montserrat:wght@600&family=Inter:wght@400;500&display=swap">
<style>
  :root {
    --page-bg: #dbe9e4;
    --brand-green: #1e6b57;
    --brand-mint: #a8dcc4;
    --paper: #ffffff;
    --text-dark: #3a3f3d;
    --text-light: #ffffff;
    --rule: #b9cfc7;
  }
  * { margin: 0; padding: 0; box-sizing: border-box; }
  html, body { width: 1200px; height: 1200px; overflow: hidden; }
  body { background: var(--page-bg); font-family: "Inter", sans-serif; }

  .brochure {
    position: absolute; left: 276px; top: 80px;
    width: 648px; height: 1040px;
    background: var(--paper);
    box-shadow: 0 12px 34px rgba(20, 70, 55, 0.18);
    overflow: hidden;
  }
  .cover-shapes { position: absolute; inset: 0; }

  .brand {
    position: absolute; left: 55px; top: 82px;
    display: flex; align-items: center; gap: 10px;
    color: var(--brand-mint); font-size: 12px; font-weight: 500;
    letter-spacing: 0.08em; text-transform: uppercase;
  }
  .brand-dot { width: 18px; height: 18px; border-radius: 50%; background: var(--brand-mint); }

  .headline {
    position: absolute; left: 55px; top: 168px;
    font-family: "Montserrat", sans-serif; font-weight: 600;
    font-size: 52px; line-height: 1.15; color: var(--text-light);
  }
  .headline-rule {
    position: absolute; left: 55px; top: 297px;
    width: 104px; height: 1.5px; background: var(--text-light); opacity: 0.8;
  }
  .tagline {
    position: absolute; left: 55px; top: 326px; width: 230px;
    font-size: 20px; line-height: 1.38; color: var(--text-light);
  }

  .body-copy {
    position: absolute; left: 55px; width: 540px;
    font-size: 16px; line-height: 1.45; color: var(--text-dark);
  }
  .body-intro { top: 574px; }
  .body-promise { top: 704px; }
  .lead-in { color: var(--brand-green); font-weight: 500; }

  .cta-row {
    position: absolute; left: 55px; top: 922px;
    display: flex; align-items: center; height: 52px;
  }
  .icon-badge {
    width: 52px; height: 52px; border-radius: 50%;
    background: var(--brand-green);
    display: flex; align-items: center; justify-content: center;
  }
  .cta-button {
    margin-left: 14px; width: 175px; height: 50px; border-radius: 25px;
    background: var(--brand-mint); color: var(--brand-green);
    font-size: 15px; font-weight: 500; letter-spacing: 0.02em;
    display: flex; align-items: center; justify-content: center;
  }
  .cta-divider { margin: 0 48px 0 42px; width: 1.5px; height: 50px; background: var(--rule); }
  .cta-note {
    margin-left: 16px; color: var(--brand-green);
    font-size: 15px; line-height: 1.35;
  }
</style>
</head>
<body>
  <article class="brochure">
    <svg class="cover-shapes" width="648" height="1040" viewBox="0 0 648 1040">
      <defs>
        <linearGradient id="houseTones" x1="0" y1="0" x2="0" y2="1">
          <stop offset="0" stop-color="#b9d3e6"/>
          <stop offset="0.45" stop-color="#e8e3dc"/>
          <stop offset="0.8" stop-color="#9a9690"/>
          <stop offset="1" stop-color="#6f8a5e"/>
        </linearGradient>
      </defs>
      <rect class="cover-photo" x="290" y="0" width="358" height="470" fill="url(#houseTones)"
            role="img" aria-label="Photo of a well-kept modern two-storey house with balconies, hedge and paved path"/>
      <polygon class="cover-panel" points="0,0 410,0 315,452 0,482" fill="var(--brand-green)"/>
      <polygon class="accent-band" points="0,482 648,427 648,445 0,512" fill="var(--brand-mint)"/>
      <polygon class="content-sheet" points="0,512 648,445 648,1040 0,1040" fill="var(--paper)"/>
    </svg>

    <div class="brand"><span class="brand-dot"></span>Hausgut Objektservice</div>

    <h1 class="headline">Carperaty<br>Service</h1>
    <div class="headline-rule"></div>
    <p class="tagline">Property management, cleaning and maintenance.</p>

    <p class="body-copy body-intro">Our property maintenance and care services include winter clearing, repairs, caretaking and regular inspections. We look after cleaning, garden care and small technical tasks so that your building stays tidy, safe and fully functional all year round, without any worries for owners.</p>

    <p class="body-copy body-promise"><span class="lead-in">Our promise:</span> a reliable partner for property managers, owner associations, companies and private owners. We plan every visit carefully, react quickly to damage and keep entrances, stairwells and outdoor areas clean and well kept. Request your individual offer or arrange an appointment with our friendly team today.</p>

    <div class="cta-row">
      <div class="icon-badge">
        <svg width="24" height="24" viewBox="0 0 24 24" fill="none" stroke="#fff" stroke-width="2" stroke-linecap="round" stroke-linejoin="round">
          <path d="M5 3h4l2 5-2.5 1.5a11 11 0 0 0 6 6L16 13l5 2v4a2 2 0 0 1-2 2A16 16 0 0 1 3 5a2 2 0 0 1 2-2z"/>
        </svg>
      </div>
      <div class="cta-button">CONTACT US</div>
      <div class="cta-divider"></div>
      <div class="icon-badge">
        <svg width="24" height="24" viewBox="0 0 24 24" fill="none" stroke="#fff" stroke-width="1.8" stroke-linejoin="round">
          <rect x="4" y="6" width="16" height="12" rx="1"/>
          <path d="M4 7l8 6 8-6"/>
        </svg>
      </div>
      <div class="cta-note">Professional<br>Service</div>
    </div>
  </article>
</body>
</html>
```